Bref créative
Lemon Badger
Cakes and Desserts
Bright & Fun-filled
Marla Tevison
Owner
2193 Brennick Ct.
Arvada, CO 80005
marla.tevison@postvale.net
Join us on Facebook!
I also need stationery that ties in with my business card.
Logo for cake company

```html
<!DOCTYPE html>
<html lang="en">
<head>
<meta charset="utf-8">
<title>Lemon Badger – Business Cards</title>
<link href="https://fonts.googleapis.com/css2?family=Open+Sans:wght@400;600;700&family=Marcellus+SC&display=swap" rel="stylesheet">
<style>
  :root {
    --backdrop: #c9a57c;
    --cocoa: #8a4526;
    --cocoa-dark: #6e3419;
    --berry: #e5388e;
    --berry-light: #f27bb5;
    --paper: #ffffff;
    --ink: #4a4a4a;
    --label: #3a2a1e;
  }
  * { box-sizing: border-box; margin: 0; padding: 0; }
  html, body { width: 1200px; height: 794px; overflow: hidden; }
  body {
    position: relative;
    background: var(--backdrop);
    font-family: "Open Sans", Arial, sans-serif;
  }
  .card {
    position: absolute;
    width: 384px;
    height: 293px;
    border-radius: 6px;
    overflow: hidden;
    box-shadow: 0 3px 8px rgba(0,0,0,.25);
  }
  .card--light { background: var(--paper); }
  .card--dark { background: var(--cocoa); }
  .front-a { left: 180px; top: 12px; }
  .front-b { left: 634px; top: 12px; }
  .back-a  { left: 180px; top: 396px; }
  .back-b  { left: 634px; top: 396px; }

  .band { position: absolute; left: 0; width: 100%; }
  .band--top { top: 0; }
  .band--bottom { bottom: 0; }
  .card--light .band { height: 9px; background: var(--cocoa); border-bottom: 3px solid var(--cocoa-dark); }
  .card--light .band--bottom { border-bottom: 0; border-top: 3px solid var(--cocoa-dark); }
  .card--dark .band { height: 12px; background: var(--berry); border-bottom: 3px solid var(--berry-light); }
  .card--dark .band--bottom { border-bottom: 0; border-top: 3px solid var(--berry-light); }

  .logo {
    position: absolute;
    display: flex;
    align-items: center;
    gap: 14px;
    padding: 0 18px;
    background: var(--paper);
    border: 3px solid var(--berry);
    border-radius: 8px;
  }
  .front-a .logo, .front-b .logo { left: 12px; top: 26px; width: 270px; height: 78px; }
  .back-a .logo, .back-b .logo { left: 62px; top: 80px; width: 260px; height: 98px; justify-content: center; }
  .logo__square { width: 38px; height: 38px; background: var(--berry); border-radius: 4px; flex: none; }
  .logo__name {
    font-family: "Open Sans", Arial, sans-serif;
    font-weight: 700;
    font-size: 27px;
    line-height: 1;
    color: var(--berry);
  }

  .holder {
    position: absolute;
    left: 0; width: 100%;
    top: 150px;
    text-align: center;
    font-weight: 600;
    font-size: 15px;
  }
  .front-a .holder { color: var(--cocoa); }
  .front-b .holder { color: var(--berry); }

  .contact {
    position: absolute;
    right: 46px;
    top: 218px;
    text-align: right;
    font-size: 11px;
    line-height: 19px;
  }
  .front-a .contact { color: var(--ink); }
  .front-b .contact { color: var(--paper); }
  .contact__key { color: var(--berry); }
  .front-b .contact__key { color: var(--berry-light); }

  .website {
    position: absolute;
    left: 0; width: 100%;
    top: 228px;
    text-align: center;
    font-size: 11px;
  }
  .back-a .website { color: var(--ink); }
  .back-b .website { color: var(--paper); }

  .caption {
    position: absolute;
    width: 384px;
    text-align: center;
    font-family: "Marcellus SC", Georgia, serif;
    font-size: 23px;
    letter-spacing: 2px;
    color: var(--label);
  }
  .caption--front-a { left: 180px; top: 322px; }
  .caption--front-b { left: 634px; top: 322px; }
  .caption--back-a  { left: 180px; top: 704px; }
  .caption--back-b  { left: 634px; top: 704px; }
</style>
</head>
<body>

  <section class="card card--light front-a">
    <div class="band band--top"></div>
    <div class="logo"><span class="logo__square"></span><span class="logo__name">Lemon Badger</span></div>
    <p class="holder">Marla Tevison</p>
    <p class="contact">
      <span class="contact__key">P:</span> (720) 555-0147 | <span class="contact__key">E:</span> marla.tevison@postvale.net<br>
      www.lemonbadgercakes.com
    </p>
    <div class="band band--bottom"></div>
  </section>
  <p class="caption caption--front-a">Business Card Front A</p>

  <section class="card card--dark front-b">
    <div class="band band--top"></div>
    <div class="logo"><span class="logo__square"></span><span class="logo__name">Lemon Badger</span></div>
    <p class="holder">Marla Tevison</p>
    <p class="contact">
      <span class="contact__key">P:</span> (720) 555-0147 | <span class="contact__key">E:</span> marla.tevison@postvale.net<br>
      www.lemonbadgercakes.com
    </p>
    <div class="band band--bottom"></div>
  </section>
  <p class="caption caption--front-b">Business Card Front B</p>

  <section class="card card--light back-a">
    <div class="logo"><span class="logo__square"></span><span class="logo__name">Lemon Badger</span></div>
    <p class="website">www.lemonbadgercakes.com</p>
  </section>
  <p class="caption caption--back-a">Business Card Back A</p>

  <section class="card card--dark back-b">
    <div class="logo"><span class="logo__square"></span><span class="logo__name">Lemon Badger</span></div>
    <p class="website">www.lemonbadgercakes.com</p>
  </section>
  <p class="caption caption--back-b">Business Card Back B</p>

</body>
</html>
```